International E-liquid manufacturer needs a brochure

We are Lindorra USA. We manufacture numerous brands of e-liquid in an ISO certified facility and distribute product across the globe. We would like to give you the creative freedom to enhance the insert we include in our sample orders. The brand we will be focusing on for this project is Vantrelle.

Vantrelle is a sub-brand of Quiltavo. The face of the brand is Tobin Marsh, someone whom is essentially a very credible celebrity/reviewer in our industry.

We would like a bi-fold brochure, that also includes a single page insert that will act as a welcome letter.

Please find an assortment of images attached for use/inspiration.

Please visit Quiltavo.com, quiltavo.com/vantrelle, and tobinmarsh.com for additional image sourcing/inspiration.

Target Market(s)

Business Owners - Vape Shops

Vantrelle is Trendy but very credible brand.

Industry/Entity Type

Industry

```html
<!DOCTYPE html>
<html lang="en">
<head>
<meta charset="utf-8">
<title>Vantrelle – Welcome Insert</title>
<link href="https://fonts.googleapis.com/css2?family=Bebas+Neue&display=swap" rel="stylesheet">
<style>
  :root {
    --paper: #ece8e1;
    --paper-line: rgba(120, 110, 100, 0.06);
    --ink: #464646;
    --ink-dark: #2b2b2b;
    --accent: #138169;
    --rule: #9a9a9a;
  }
  * { margin: 0; padding: 0; box-sizing: border-box; }
  html, body { width: 855px; height: 1200px; overflow: hidden; }
  body {
    font-family: "Bebas Neue", "Arial Narrow", sans-serif;
    background-color: var(--paper);
    background-image:
      repeating-linear-gradient(0deg, var(--paper-line) 0 1px, transparent 1px 4px),
      repeating-linear-gradient(90deg, var(--paper-line) 0 1px, transparent 1px 4px);
  }
  .insert { position: relative; width: 855px; height: 1200px; }
  .brand-name {
    position: absolute; left: 0; right: 0; top: 300px;
    text-align: center; font-size: 120px; line-height: 1;
    letter-spacing: 4px; color: var(--ink-dark);
  }
  .hatch-rule {
    position: absolute; left: 245px; width: 365px; height: 12px;
    background: repeating-linear-gradient(115deg, var(--rule) 0 2px, transparent 2px 6px);
  }
  .hatch-rule.top { top: 570px; }
  .hatch-rule.bottom { top: 970px; }
  .welcome {
    position: absolute; left: 0; right: 0; top: 612px;
    text-align: center; font-size: 104px; line-height: 114px;
    color: var(--ink); letter-spacing: 1px;
  }
  .welcome .highlight { color: var(--accent); }
  .promise {
    position: absolute; left: 0; right: 0; top: 1010px;
    text-align: center; font-size: 23px; letter-spacing: 0.5px;
    color: var(--ink-dark);
  }
</style>
</head>
<body>
  <main class="insert">
    <div class="brand-name">Vantrelle</div>
    <div class="hatch-rule top"></div>
    <h1 class="welcome">
      Welcome,<br>
      To Experience<br>
      <span class="highlight">The Max</span>
    </h1>
    <div class="hatch-rule bottom"></div>
    <p class="promise">Max VG * Max Vapor * Max Flavour</p>
  </main>
</body>
</html>
```